"Recently Leased" flyer for real estate agency

Looking to have a Recently Leased flyer designed. This will be delivered to apartments and houses closely situated to a property we have recently leased. The idea is to get the attention of owner/landlords in the area that may be considering leasing their property in the future and inform them of the great work we are doing locally. I would like the design to be a two sided flyer using the photoshop (PSD) template below (we would like to be able to edit this once complete should we need to update copy etc in the future). I would like the front page to look like our "for lease sign with the leased sticker on it and copy, I dont want it to look like a typical junk mail flyer.

Target Market(s)

Property owners and investors, male and female aged 28-70

Industry/Entity Type

Real Estate

Font styles to use
Sans Serif

Colors

Designer to choose colors to be used in the design.

Requirements
Must have
• Harbor Keystone Logo
• Contact information
• Copy supplied
Nice to have
• Slick, clean design,
Should not have
• too many colours or too busy a design.
• NO PROPERTY PHOTOS ON FRONT - I want this to be generic and not relate to a specific property image which might confuse people.

```html
<!DOCTYPE html>
<html lang="en">
<head>
<meta charset="utf-8">
<title>Recently Leased Flyer – Harbor Keystone</title>
<link href="https://fonts.googleapis.com/css2?family=Roboto+Condensed:wght@700&family=Source+Sans+3:wght@300;400;600;700&display=swap" rel="stylesheet">
<style>
  :root{
    --teal:#1f7f8c;
    --red:#b8232b;
    --ink:#3a3a3a;
    --body:#4a4a4a;
    --paper:#ffffff;
    --backdrop:#e9eaec;
  }
  *{box-sizing:border-box;margin:0;padding:0}
  html,body{width:1200px;height:1200px;overflow:hidden;background:var(--backdrop)}
  body{position:relative;font-family:"Source Sans 3",sans-serif;color:var(--body)}
  .flyer{position:absolute;top:98px;width:463px;height:1006px;background:var(--paper);box-shadow:0 4px 18px rgba(0,0,0,.18);overflow:hidden}
  .flyer--front{left:100px}
  .flyer--back{left:638px}

  .hero{position:absolute;left:0;top:0;width:463px;height:387px;
    background:linear-gradient(180deg,#cfe9f7 0%,#e9f3f8 30%,#9aa3a8 50%,#5e8a4a 72%,#7fa85a 100%)}
  .brand{position:absolute;left:0;right:0;top:56px;text-align:center;font-family:"Source Sans 3",sans-serif;font-weight:700;font-size:29px;letter-spacing:.5px;color:#111}

  .headline{position:absolute;left:28px;top:400px;right:24px}
  .headline__lead{font-family:"Roboto Condensed",sans-serif;font-size:33px;line-height:38px;color:var(--teal)}
  .headline__lead span{color:var(--red)}
  .headline__line{font-size:26px;line-height:30px;font-weight:300;color:var(--ink)}
  .headline__line--teal{color:var(--teal)}
  .headline__line--bold{font-weight:700;font-family:"Roboto Condensed",sans-serif;font-size:25px}

  .intro{position:absolute;left:28px;right:28px;top:540px;font-size:14.3px;line-height:18px;font-weight:400}
  .points{list-style:none;position:absolute;left:28px;right:26px;font-size:13.6px;line-height:17px;font-weight:400}
  .points li{position:relative;padding-left:18px;margin-bottom:7px}
  .points li::before{content:"»";position:absolute;left:0;top:-2px;font-size:17px;font-weight:700;color:var(--teal)}
  .points li.plain::before{content:none}
  .flyer--front .points{top:606px}
  .flyer--back .points{top:531px;text-align:justify}

  .lead-in{position:absolute;left:28px;right:29px;top:452px;font-size:14.3px;line-height:18.5px;font-weight:600;color:var(--ink);text-align:justify}

  .gallery__main{position:absolute;left:28px;top:28px;width:406px;height:264px;background:linear-gradient(135deg,#6f7479 0%,#b5694a 45%,#c9b59a 70%,#4b5157 100%)}
  .gallery__thumb{position:absolute;top:307px;width:128px;height:119px;box-shadow:0 3px 4px rgba(0,0,0,.25)}
  .gallery__thumb--bed{left:28px;background:linear-gradient(160deg,#d9d1bf,#efe9dd 60%,#b89263)}
  .gallery__thumb--living{left:167px;background:linear-gradient(160deg,#6c7175,#9d9a93 55%,#b88b5a)}
  .gallery__thumb--kitchen{left:306px;background:linear-gradient(160deg,#f2f2f0,#e0e0de 55%,#2e2e2e)}
  .leased{position:absolute;width:46px;height:46px;overflow:hidden}
  .leased span{position:absolute;left:-20px;top:12px;width:86px;transform:rotate(-45deg);background:var(--red);color:#fff;font-size:8px;font-weight:600;text-align:center;line-height:12px;letter-spacing:.5px}

  .contact__photo{position:absolute;left:28px;top:797px;width:94px;height:106px;border:4px solid var(--teal);background:linear-gradient(180deg,#9fb4c3,#c7a58c 55%,#8aa3bd);z-index:2;outline:2px solid #fff;outline-offset:-7px}
  .contact__band{position:absolute;left:0;right:0;top:869px;height:50px;background:var(--teal);color:#fff;padding:7px 0 0 138px}
  .contact__name{font-family:"Roboto Condensed",sans-serif;font-size:20px;line-height:21px}
  .contact__role{font-size:15px;font-weight:300;line-height:18px}
  .contact__text{position:absolute;left:138px;right:28px;top:797px;font-size:12.4px;line-height:16px;text-align:justify}
  .contact__title{font-weight:700;font-size:15px;color:var(--teal);line-height:16px}

  .footer{position:absolute;left:28px;right:20px;top:932px;display:flex;font-size:12.6px;line-height:16px;color:var(--body)}
  .footer__office{width:178px;padding-right:10px;border-right:1px solid #bbb}
  .footer__reach{padding-left:16px}
  .footer strong{font-weight:600;color:var(--ink)}
  .footer .row{display:flex;align-items:center;gap:5px}
  .footer svg{width:11px;height:11px;fill:var(--teal);flex:none}
  .footer .indent{padding-left:19px}
</style>
</head>
<body>

<section class="flyer flyer--front">
  <div class="hero" role="img" aria-label="Photo of modern terraced townhouses with landscaped gardens under a blue sky"></div>
  <div class="brand">HARBOR KEYSTONE</div>

  <div class="headline">
    <div class="headline__lead">WE RECENTLY <span>LEASED</span></div>
    <div class="headline__line">a property in your building or street.</div>
    <div class="headline__line headline__line--teal">Attracting a great reliable tenant and</div>
    <div class="headline__line headline__line--bold">fantastic return for the owner.</div>
  </div>

  <p class="intro">We received a high number of enquires and applications for this property and have a database of screened and qualified tenants looking to lease in your area.</p>

  <ul class="points">
    <li>On average we lease properties 2 weeks faster than the Coastal District average</li>
    <li>Strong database of tenants actively looking in the area</li>
    <li>All we do is lease property, no sales – so tenanting and managing your property is our priority</li>
    <li>90 day money back guarantee on our level of service</li>
    <li>Highly competitive, simple all-inclusive pricing.</li>
    <li class="plain">Experience the difference of a property management specialist</li>
  </ul>

  <div class="contact__photo" role="img" aria-label="Portrait photo of the property manager"></div>
  <div class="contact__text">
    <div class="contact__title">CONTACT SAM</div>
    to get your free rental appraisal or transfer your existing investment to an agency that will give it the attention it deserves and maxamise your return.
  </div>
  <div class="contact__band">
    <div class="contact__name">SAM CARVER</div>
    <div class="contact__role">Director/Property Manager</div>
  </div>

  <div class="footer">
    <div class="footer__office">
      <div class="row"><svg viewBox="0 0 12 12"><path d="M6 1 0 6h2v5h3V8h2v3h3V6h2z"/></svg><strong>Harbor Keystone Agency</strong></div>
      <div class="indent">Level 1, 18 Marlow Rd,</div>
      <div class="indent">Fairhaven NSW 2099</div>
    </div>
    <div class="footer__reach">
      <div class="row"><svg viewBox="0 0 12 12"><path d="M2 1h3l1 3-2 1a7 7 0 0 0 3 3l1-2 3 1v3c-6 0-9-3-9-9z"/></svg><strong>0400 555 217</strong></div>
      <div class="row"><svg viewBox="0 0 12 12"><path d="M1 3h10v7H1zM1 3l5 4 5-4" stroke="#fff" stroke-width=".8"/></svg>sam@harborkeystone.com.au</div>
      <div class="row"><svg viewBox="0 0 12 12"><circle cx="6" cy="6" r="5"/></svg>www.harborkeystone.com.au</div>
    </div>
  </div>
</section>

<section class="flyer flyer--back">
  <div class="gallery__main" role="img" aria-label="Photo of an apartment balcony with glass table and barbecue"></div>
  <div class="leased" style="left:28px;top:28px"><span>LEASED</span></div>
  <div class="gallery__thumb gallery__thumb--bed" role="img" aria-label="Photo of a bedroom"></div>
  <div class="leased" style="left:28px;top:307px"><span>LEASED</span></div>
  <div class="gallery__thumb gallery__thumb--living" role="img" aria-label="Photo of a living and dining room"></div>
  <div class="leased" style="left:167px;top:307px"><span>LEASED</span></div>
  <div class="gallery__thumb gallery__thumb--kitchen" role="img" aria-label="Photo of a kitchen"></div>
  <div class="leased" style="left:306px;top:307px"><span>LEASED</span></div>

  <p class="lead-in">The fundamental idea behind Harbor Keystone Agency was to give landlords a simple and confidence inspiring experience. We achieve this through:</p>

  <ul class="points">
    <li>Unique marketing that goes beyond the standard listing sites and has seen our average days-on-market at 5.9days for 2018.</li>
    <li>A simple, yet competitive fee structure.</li>
    <li>Excellent customer service through an experienced professional property manager.</li>
    <li>Sound advice and communication through out the leasing and management process.</li>
    <li>A simple yet powerful landlord portal which enables owners to view media rich inspection reports, financial reports and maintenance progress at anytime.</li>
    <li>We then back our service promise with a 90day money back guarantee.</li>
  </ul>

  <div class="contact__photo" role="img" aria-label="Portrait photo of the property manager"></div>
  <div class="contact__text">If you have been considering leasing your property, purchasing a local investment or aren't happy with your current managing agency, please don't hesitate to contact your local rental specialist for more information:</div>
  <div class="contact__band">
    <div class="contact__name">SAM CARVER</div>
    <div class="contact__role">Director/Property Manager</div>
  </div>

  <div class="footer">
    <div class="footer__office">
      <div class="row"><svg viewBox="0 0 12 12"><path d="M6 1 0 6h2v5h3V8h2v3h3V6h2z"/></svg><strong>Harbor Keystone Agency</strong></div>
      <div class="indent">Level 1, 18 Marlow Rd,</div>
      <div class="indent">Fairhaven NSW 2099</div>
    </div>
    <div class="footer__reach">
      <div class="row"><svg viewBox="0 0 12 12"><path d="M2 1h3l1 3-2 1a7 7 0 0 0 3 3l1-2 3 1v3c-6 0-9-3-9-9z"/></svg><strong>0400 555 217</strong></div>
      <div class="row"><svg viewBox="0 0 12 12"><path d="M1 3h10v7H1zM1 3l5 4 5-4" stroke="#fff" stroke-width=".8"/></svg>sam@harborkeystone.com.au</div>
      <div class="row"><svg viewBox="0 0 12 12"><circle cx="6" cy="6" r="5"/></svg>www.harborkeystone.com.au</div>
    </div>
  </div>
</section>

</body>
</html>
```